PowerPoint Master for IT company (lumoGrid GmbH)

As IT company we work in the fields Mobile, Big Data, Predictive Maintenance, Industry 4.0 and Data Science for the german Rail company "Nordwerk Schiene". We already have a Logo, coloring and a website (Attached Files).

What we need is a clear, professional and simple Design (nothing fancy) for PowerPoint/Word Master and Business Cards. Stockphotos from https://bildarchiv.nordwerkschiene.example/ can be used beside the attached logos.

We are a german company but would need either an universal or DE and EN template for PoerPoint.

Target Market(s)

IT, B2B, Rail companies, Industry

Contact Information for Business Card

- Logo
- Company Name
- Name
- Position
- Address
- Phone
- Mail

Font styles to use
Sans Serif

```html
<!DOCTYPE html>
<html lang="de">
<head>
<meta charset="utf-8">
<title>lumoGrid GmbH – PowerPoint Master</title>
<link href="https://fonts.googleapis.com/css2?family=Open+Sans:wght@300;400;600;700&display=swap" rel="stylesheet">
<style>
  :root {
    --canvas: #d9d9d9;
    --navy: #283f89;
    --navy-deep: #1f3274;
    --band: #5a6ca8;
    --band-light: #4f86cf;
    --white: #ffffff;
    --ink-soft: #8a8f99;
    --ink-dark: #3a3d44;
  }
  * { box-sizing: border-box; margin: 0; padding: 0; }
  html, body { width: 1200px; height: 900px; overflow: hidden; }
  body {
    background: var(--canvas);
    font-family: "Open Sans", Arial, sans-serif;
    position: relative;
  }
  .slide {
    position: absolute;
    width: 351px;
    height: 198px;
    overflow: hidden;
    background: var(--navy);
    color: var(--white);
  }
  .slide--intro { left: 46px; top: 135px; }
  .slide--about { left: 425px; top: 135px; background: var(--white); color: var(--ink-soft); }
  .slide--career { left: 800px; top: 135px; }
  .slide--jobs { left: 46px; top: 354px; }
  .slide--closing { left: 428px; top: 354px; }
  .slide__decor { position: absolute; inset: 0; width: 100%; height: 100%; }

  /* intro */
  .check { position: absolute; left: 84px; top: 69px; width: 44px; height: 44px; }
  .intro__text { position: absolute; left: 150px; top: 66px; width: 170px; font-size: 6.5px; line-height: 1.4; }
  .intro__text p + p { margin-top: 7px; }
  .intro__headline { position: absolute; left: 150px; top: 129px; font-size: 12.5px; font-weight: 700; }

  /* about */
  .about__text { position: absolute; left: 86px; top: 51px; width: 210px; font-size: 6.5px; line-height: 1.75; }
  .about__footer { position: absolute; right: 22px; bottom: 5px; display: flex; align-items: center; gap: 6px; font-size: 6px; color: var(--ink-dark); }
  .about__parent { font-weight: 700; font-size: 6px; }
  .about__slash { width: 2px; height: 14px; background: var(--ink-dark); transform: skewX(-20deg); margin: 0 6px; }
  .about__page { color: var(--ink-soft); font-size: 5px; }

  /* career */
  .career__photo {
    position: absolute; inset: 0;
    background: linear-gradient(120deg, #6d7fa8 0%, #3d5a98 40%, #7aa6d9 65%, #1c2f5e 100%);
  }
  .career__content { position: absolute; left: 25px; top: 72px; width: 110px; }
  .career__title { font-size: 14px; font-weight: 700; line-height: 1.2; }
  .rule { width: 18px; height: 1.5px; background: var(--white); margin: 8px 0; }
  .career__icon { width: 12px; height: 14px; display: block; margin-bottom: 4px; }
  .career__role { font-size: 6.5px; font-weight: 700; margin: 4px 0 3px; }
  .career__copy { font-size: 4.5px; line-height: 1.45; }

  /* jobs */
  .team-icon { position: absolute; left: 97px; top: 44px; width: 34px; height: 30px; }
  .jobs__content { position: absolute; left: 152px; top: 34px; }
  .jobs__title { font-size: 14px; font-weight: 700; line-height: 1.2; }
  .jobs__list { list-style: none; font-size: 6.5px; line-height: 1.65; margin-top: 12px; }
  .jobs__list li::before { content: "✓"; margin-right: 4px; }
  .jobs__list .indent { padding-left: 10px; }

  /* closing */
  .closing__photo {
    position: absolute; inset: 0;
    background: linear-gradient(160deg, #8ea6c4 0%, #4f6d86 35%, #3d5e5a 65%, #2e4a6a 100%);
  }
  .closing__tint { position: absolute; inset: 0; background: rgba(40, 63, 137, 0.55); }
  .closing__content { position: absolute; left: 0; right: 0; top: 36px; text-align: center; }
  .brand { display: inline-flex; align-items: center; gap: 6px; font-size: 17px; font-weight: 300; letter-spacing: 1px; }
  .brand__dot { width: 13px; height: 13px; border-radius: 50%; background: var(--white); }
  .closing__thanks { font-size: 15px; font-weight: 700; margin-top: 16px; }
  .closing__content .rule { margin: 4px auto 8px; }
  .closing__label { font-size: 6px; font-weight: 700; }
  .contact-icons { display: flex; justify-content: center; gap: 7px; margin: 10px 0 6px; }
  .contact-icons svg { width: 11px; height: 11px; }
  .contact-lines { font-size: 4.5px; line-height: 1.4; }
</style>
</head>
<body>

  <section class="slide slide--intro">
    <svg class="slide__decor" viewBox="0 0 351 198">
      <polygon points="0,198 13,198 81,0 67,0" fill="var(--band)"/>
      <line x1="32" y1="112" x2="49" y2="60" stroke="var(--white)" stroke-width="4"/>
    </svg>
    <svg class="check" viewBox="0 0 44 44">
      <circle cx="22" cy="22" r="21" fill="none" stroke="var(--white)" stroke-width="1"/>
      <polyline points="13,22 19.5,29 31,14" fill="none" stroke="var(--white)" stroke-width="2.4"/>
    </svg>
    <div class="intro__text">
      <p>Du suchst eine spannende Herausforderung?</p>
      <p>Willst Du bei einem jungen Tech-Unternehmen die Mobilitäts-Infrastruktur mitgestalten und verbessern?</p>
    </div>
    <h2 class="intro__headline">Dann bewirb Dich bei uns!</h2>
  </section>

  <section class="slide slide--about">
    <svg class="slide__decor" viewBox="0 0 351 198">
      <polygon points="0,198 12,198 80,0 68,0" fill="var(--band)"/>
      <line x1="35" y1="112" x2="50" y2="60" stroke="var(--ink-dark)" stroke-width="4"/>
    </svg>
    <p class="about__text">Als Arbeitgeber verbinden wir die Atmosphäre und den Spirit eines jungen, innovativen Unternehmens mit der Sicherheit, der Vertriebskraft und den Karrieremöglichkeiten eines großen Konzerns. Wir schaffen als Pionier eine Plattform für die Verwaltung der Infrastruktur der Zukunft.</p>
    <div class="about__footer">
      <span>Ein Unternehmen</span>
      <span class="about__parent">Nordwerk Schiene</span>
      <span class="about__slash"></span>
      <span class="about__page">11</span>
    </div>
  </section>

  <section class="slide slide--career">
    <div class="career__photo" role="img" aria-label="Foto: Laptop mit Programmcode auf dem Bildschirm"></div>
    <svg class="slide__decor" viewBox="0 0 351 198">
      <polygon points="0,0 100,0 164,198 0,198" fill="var(--navy)" opacity="0.92"/>
      <polygon points="100,0 111,0 175,198 164,198" fill="var(--band-light)"/>
      <line x1="130" y1="60" x2="143" y2="110" stroke="var(--white)" stroke-width="3"/>
    </svg>
    <div class="career__content">
      <h2 class="career__title">Bei uns<br>arbeiten</h2>
      <div class="rule"></div>
      <svg class="career__icon" viewBox="0 0 12 14">
        <path d="M3 1v12M0.5 10.5L3 13l2.5-2.5M9 13V1M6.5 3.5L9 1l2.5 2.5" fill="none" stroke="var(--white)" stroke-width="1.3"/>
      </svg>
      <p class="career__role">Software Developer</p>
      <p class="career__copy">Ob Frontend, Backend oder Fullstack: Unsere Entwickler sorgen dafür, dass unsere Diagnoseplattform fortwährend optimiert, neu entwickelt und die wichtigsten Informationen auf den Punkt visualisiert werden.</p>
    </div>
  </section>

  <section class="slide slide--jobs">
    <svg class="slide__decor" viewBox="0 0 351 198">
      <polygon points="0,198 13,198 81,0 67,0" fill="var(--band)"/>
      <line x1="32" y1="112" x2="49" y2="60" stroke="var(--white)" stroke-width="4"/>
    </svg>
    <svg class="team-icon" viewBox="0 0 34 30">
      <circle cx="17" cy="8" r="6" fill="var(--white)"/>
      <path d="M7 28c0-7 4-11 10-11s10 4 10 11z" fill="var(--white)"/>
      <circle cx="6" cy="10" r="4" fill="var(--white)"/>
      <path d="M0 24c0-5 2.5-8 6-8 1.5 0 2.5.5 3 1-2 2-3 4.5-3 7z" fill="var(--white)"/>
      <circle cx="28" cy="10" r="4" fill="var(--white)"/>
      <path d="M34 24c0-5-2.5-8-6-8-1.5 0-2.5.5-3 1 2 2 3 4.5 3 7z" fill="var(--white)"/>
    </svg>
    <div class="jobs__content">
      <h2 class="jobs__title">Zur Verstärkung unseres<br>Teams in Mainz suchen wir</h2>
      <div class="rule"></div>
      <ul class="jobs__list">
        <li>Mitarbeiter Operations &amp;<br><span class="indent">Administration (W/M)</span></li>
        <li>Javascript Frontend Architekt (W/M)</li>
        <li>Mitarbeiter im HelpDesk (W/M)</li>
        <li>Java-Softwareentwickler (W/M)</li>
        <li>Software-Tester (W/M)</li>
      </ul>
    </div>
  </section>

  <section class="slide slide--closing">
    <div class="closing__photo" role="img" aria-label="Foto: Hochgeschwindigkeitszug fährt durch grüne Landschaft"></div>
    <div class="closing__tint"></div>
    <svg class="slide__decor" viewBox="0 0 351 198">
      <polygon points="0,198 13,198 81,0 67,0" fill="var(--band)" opacity="0.8"/>
      <line x1="32" y1="112" x2="49" y2="60" stroke="var(--white)" stroke-width="4"/>
    </svg>
    <div class="closing__content">
      <div class="brand"><span>LUMOGRID</span><span class="brand__dot"></span></div>
      <h2 class="closing__thanks">DANKE DIR</h2>
      <div class="rule"></div>
      <p class="closing__label">KONTAKT</p>
      <div class="contact-icons">
        <svg viewBox="0 0 11 11"><circle cx="5.5" cy="5.5" r="5" fill="none" stroke="var(--white)" stroke-width="0.7"/><rect x="3" y="3.8" width="5" height="3.5" fill="none" stroke="var(--white)" stroke-width="0.6"/><polyline points="3,3.8 5.5,5.8 8,3.8" fill="none" stroke="var(--white)" stroke-width="0.6"/></svg>
        <svg viewBox="0 0 11 11"><circle cx="5.5" cy="5.5" r="5" fill="none" stroke="var(--white)" stroke-width="0.7"/><circle cx="5.5" cy="5.5" r="2.6" fill="none" stroke="var(--white)" stroke-width="0.6"/><line x1="2.9" y1="5.5" x2="8.1" y2="5.5" stroke="var(--white)" stroke-width="0.5"/></svg>
        <svg viewBox="0 0 11 11"><path d="M5.5 2a2.3 2.3 0 0 1 2.3 2.3c0 1.8-2.3 4.5-2.3 4.5S3.2 6.1 3.2 4.3A2.3 2.3 0 0 1 5.5 2z" fill="var(--white)"/><circle cx="5.5" cy="4.3" r="0.9" fill="var(--navy)"/></svg>
      </div>
      <div class="contact-lines">
        <p>kontakt@lumogrid.example</p>
        <p>www.lumogrid.example</p>
        <p>Adresse</p>
      </div>
    </div>
  </section>

</body>
</html>
```